依頼詳細
1つ1つ角折包装された饅頭を3個トレーに入れ、ピロー包装しております。
そのパッケージデザインを依頼させて頂きます。

・商品名は「ほたるまんじゅう」です。
・商品名は縦書き、読み易い和風のフォントでお願いします。
・デザインはシンプルかつ和風で可愛らしいイメージです。
(ただし、30~50代の主婦がメインターゲットなので、「和」寄りになりすぎず、可愛らしいイメージも加えて下さい)
・お月見で販売するので、お月見と関連付けたデザインにして下さい。
・また白い饅頭を「うさぎ」に見立てたようなデザインでお願いします。
・添付したこもれび堂の新しいロゴマークを入れてください。
記載項目
商品がある程度見えるデザインが望ましいので、ベースは透明でお願いします。

巾265×ピッチ250(mm)
表面デザイン可能サイズ 縦170×横75(mm)
色数:4色以内(白・黒・特色2色)
包装形態:トレー三方ピロー包装

【表記するもの】
・商品名「ほたるまんじゅう」
・「小豆こしあん」
・会社ロゴ(縦書き)

なお、商品の左上部分に賞味期限表示を印字するので、縦15×横40(mm)の白べた(丸角)を入れてください。
実際の商品のイメージを添付しております。そちらをデザインに入れて提案して下さい。
希望イメージ
シンプル 複雑
単色 カラフル
暗い 明るい
日常 高級
遊び心 厳粛
未来的 伝統的
女性的 男性的
希望する色
青系、黄・オレンジ系、上記の色は使用必須ではありません。お月見らしい色合いにしてください。
納品ファイル
• イラストレーター形式 (.ai)
補足説明
■ 選んだ理由

シンプルかつ可愛く、饅頭をウサギに見立てたいというこちらの意向を分かりやすく表現して下さっていた点がとても評価が高かったです。

■ 提案者全員のお礼・コメント

沢山のご提案ありがとうございました。
通常では考えられないような、様々な角度からの提案があり、
とても良いコンペになりました。

本当にありがとうございました。

```html
<!DOCTYPE html>
<html lang="ja">
<head>
<meta charset="utf-8">
<title>ほたるまんじゅう パッケージ</title>
<link rel="stylesheet" href="https://fonts.googleapis.com/css2?family=Yuji+Syuku&family=Zen+Maru+Gothic:wght@700&display=swap">
<style>
  :root {
    --bg: #eef3ef;
    --film: rgba(236, 240, 238, 0.9);
    --film-edge: #c9d0cc;
    --contents-top: #f4efd9;
    --contents-bottom: #e6e2cf;
    --moon: #fbef86;
    --label-white: #ffffff;
    --ink: #1c1a17;
    --badge-red: #e0252b;
    --badge-text: #ffffff;
    --rabbit-white: #ffffff;
  }
  html, body {
    margin: 0;
    width: 835px;
    height: 1200px;
    overflow: hidden;
    background: var(--bg);
  }
  .canvas {
    position: relative;
    width: 835px;
    height: 1200px;
  }
  .pack {
    position: absolute;
    left: 167px;
    top: 28px;
    width: 514px;
    height: 1140px;
    background: var(--film);
    border: 2px solid var(--film-edge);
    border-radius: 6px;
    overflow: hidden;
  }
  .pack-contents {
    position: absolute;
    left: 50px;
    top: 120px;
    width: 414px;
    height: 960px;
    border-radius: 40px;
    background: linear-gradient(180deg, var(--contents-top), var(--contents-bottom));
  }
  .moon {
    position: absolute;
    left: 16px;
    top: 50px;
    width: 456px;
    height: 456px;
    border-radius: 50%;
    background: var(--moon);
  }
  .date-label {
    position: absolute;
    left: 89px;
    top: 55px;
    width: 161px;
    height: 84px;
    background: var(--label-white);
    border-radius: 8px;
  }
  .title {
    position: absolute;
    writing-mode: vertical-rl;
    font-family: "Yuji Syuku", serif;
    color: var(--ink);
    margin: 0;
    line-height: 1;
  }
  .title-main {
    left: 250px;
    top: 100px;
    font-size: 112px;
    letter-spacing: -4px;
  }
  .title-sub {
    left: 168px;
    top: 230px;
    font-size: 58px;
    letter-spacing: 2px;
  }
  .bean-badge {
    position: absolute;
    left: 222px;
    top: 444px;
    width: 168px;
    height: 112px;
    border-radius: 50%;
    background: var(--badge-red);
    color: var(--badge-text);
    font-family: "Zen Maru Gothic", sans-serif;
    font-weight: 700;
    text-align: center;
    display: flex;
    flex-direction: column;
    justify-content: center;
    gap: 4px;
  }
  .bean-badge .badge-note { font-size: 17px; letter-spacing: 2px; }
  .bean-badge .badge-flavor { font-size: 27px; }
  .rabbit-face {
    position: absolute;
    left: 22px;
    top: 610px;
    width: 390px;
    height: 390px;
    border-radius: 50%;
    background: var(--rabbit-white);
  }
  .maker {
    position: absolute;
    left: 368px;
    top: 665px;
    display: flex;
    flex-direction: column;
    align-items: center;
    gap: 14px;
  }
  .maker-name {
    writing-mode: vertical-rl;
    font-family: "Yuji Syuku", serif;
    font-size: 52px;
    color: var(--ink);
    line-height: 1;
    margin: 0;
  }
  .maker-mark {
    width: 40px;
    height: 40px;
    border-radius: 50%;
    background: var(--badge-red);
  }
</style>
</head>
<body>
  <main class="canvas">
    <section class="pack">
      <div class="pack-contents" role="img" aria-label="トレーに並んだ三つの白いまんじゅう"></div>
      <div class="moon"></div>
      <div class="date-label" aria-label="賞味期限表示欄"></div>
      <h1 class="title title-main">ほたる</h1>
      <p class="title title-sub">まんじゅう</p>
      <div class="bean-badge">
        <span class="badge-note">自家炊き</span>
        <span class="badge-flavor">小豆こしあん</span>
      </div>
      <div class="rabbit-face" role="img" aria-label="まんじゅうをうさぎに見立てた耳と赤い目のイラスト"></div>
      <div class="maker">
        <p class="maker-name">こもれび堂</p>
        <span class="maker-mark"></span>
      </div>
    </section>
  </main>
</body>
</html>
```